Business Card for premium dental clinic

We are a premium dental clinic based in Brasov, Romania with more than 15 year on the market, providing quality dental treatment made by a team of more specialized dentists, working with modern equipment as a solution to beautiful and healthy teeth.

Our current logo for the clinic use 2 square with colors black and gold - dr Corbescu - studio, using family fonts Bodoni, Myriad Pro and Segoe Print.
Depending on the printing we used some gold CMYK background or gold foil picture background or a gold gradient.
We want a business card:
- eye catching business card
- distinguished business card
- premium design
- to keep the color scheme of black and gold
- to attract the customers to spent time reading the information
- modern concept

```html
<!DOCTYPE html>
<html lang="ro">
<head>
<meta charset="utf-8">
<title>dr Corbescu – business card</title>
<link rel="stylesheet" href="https://fonts.googleapis.com/css2?family=Montserrat:wght@400;500;600;700&display=swap">
<style>
  :root {
    --stage: #ecebe7;
    --charcoal: #2a2d30;
    --charcoal-light: #3a3e42;
    --black: #111111;
    --gold: #c9a233;
    --gold-dark: #a98521;
    --paper: #ffffff;
    --ink: #3b3b3b;
    --ink-soft: #5a5a5a;
    --web-ink: #55595e;
  }
  * { box-sizing: border-box; margin: 0; padding: 0; }
  html, body { width: 1200px; height: 866px; overflow: hidden; }
  body {
    background: var(--stage);
    font-family: "Montserrat", Arial, sans-serif;
    position: relative;
  }
  .card {
    position: absolute;
    width: 560px;
    height: 320px;
    overflow: hidden;
    box-shadow: 0 10px 28px rgba(0,0,0,.18);
  }

  /* Back side */
  .card--back {
    left: 40px; top: 80px;
    background: linear-gradient(160deg, var(--charcoal) 0%, var(--charcoal-light) 100%);
  }
  .card--back .brand {
    position: absolute;
    left: 0; right: 0; top: 104px;
    display: flex;
    justify-content: center;
    align-items: center;
    gap: 16px;
  }
  .card--back .brand .mark {
    width: 30px; height: 30px;
    background: var(--gold);
  }
  .card--back .brand-name {
    color: var(--paper);
    font-size: 30px;
    font-weight: 500;
    letter-spacing: .5px;
  }
  .card--back .website {
    position: absolute;
    left: 0; right: 0; top: 214px;
    text-align: center;
    color: var(--web-ink);
    font-size: 15px;
    font-weight: 700;
    letter-spacing: 3px;
  }
  .card--back .gold-strip {
    position: absolute;
    left: 0; right: 0; bottom: 0;
    height: 70px;
    background: var(--gold);
    border-top: 1px solid var(--gold-dark);
  }

  /* Front side */
  .card--front {
    left: 600px; top: 466px;
    background: var(--paper);
  }
  .card--front .brand {
    position: absolute;
    left: 36px; top: 40px;
    display: flex;
    align-items: center;
    gap: 12px;
  }
  .card--front .brand .mark {
    width: 26px; height: 26px;
    background: var(--gold);
  }
  .card--front .brand-name {
    color: var(--black);
    font-size: 20px;
    font-weight: 500;
  }
  .card--front .person {
    position: absolute;
    left: 36px; top: 150px;
  }
  .person .name {
    color: var(--gold);
    font-size: 26px;
    font-weight: 700;
    letter-spacing: .3px;
  }
  .person .role {
    color: var(--ink-soft);
    font-size: 14px;
    font-weight: 500;
    margin-top: 2px;
  }
  .contacts {
    position: absolute;
    left: 36px; top: 226px;
    list-style: none;
    color: var(--ink);
    font-size: 14px;
  }
  .contacts li {
    display: flex;
    align-items: center;
    gap: 12px;
    height: 24px;
  }
  .contacts svg { width: 14px; height: 14px; fill: var(--gold); }
  .address {
    position: absolute;
    right: 30px; top: 200px;
    text-align: right;
    color: var(--ink);
    font-size: 13px;
    line-height: 1.35;
    font-style: normal;
  }
  .card--front .gold-strip {
    position: absolute;
    left: 0; right: 0; bottom: 0;
    height: 24px;
    background: var(--gold);
  }
</style>
</head>
<body>

<section class="card card--back" aria-label="Business card back">
  <div class="brand">
    <span class="mark"></span>
    <span class="brand-name">dr Corbescu</span>
  </div>
  <p class="website">www.drcorbescu.ro</p>
  <div class="gold-strip"></div>
</section>

<section class="card card--front" aria-label="Business card front">
  <div class="brand">
    <span class="mark"></span>
    <span class="brand-name">dr Corbescu</span>
  </div>

  <div class="person">
    <p class="name">Ilinca Marin</p>
    <p class="role">Doctor</p>
  </div>

  <ul class="contacts">
    <li>
      <svg viewBox="0 0 24 24" aria-hidden="true"><path d="M6.6 10.8a15.1 15.1 0 0 0 6.6 6.6l2.2-2.2a1 1 0 0 1 1-.25 11.4 11.4 0 0 0 3.6.57 1 1 0 0 1 1 1V20a1 1 0 0 1-1 1A17 17 0 0 1 3 4a1 1 0 0 1 1-1h3.5a1 1 0 0 1 1 1c0 1.25.2 2.45.57 3.57a1 1 0 0 1-.25 1z"/></svg>
      <span>+40 268 555 019</span>
    </li>
    <li>
      <svg viewBox="0 0 24 24" aria-hidden="true"><path d="M2 5h20v14H2zm2 2v.4l8 5.2 8-5.2V7zm0 2.8V17h16V9.8l-8 5.2z"/></svg>
      <span>i.marin@drcorbescu.ro</span>
    </li>
  </ul>

  <address class="address">Strada Livezii nr 7<br>500180 Brașov</address>

  <div class="gold-strip"></div>
</section>

</body>
</html>
```